We need a poster designed for use on facebook, as well as to print out for advertising in local noticeboards and shop windows.
The poster will advertise the Fernhollow Turf Society 30th Anniversary Ball.
the ball will be held on the 28th April 2018 at the Fernhollow Community Hall.
Time will be 630pm till late. Ticket Price is $120 which includes 3 course dinner, drinks on arrival and entertainment during the evening.
Additional details will need to be added to the poster at a later date.
The fernhollow Turf Society is a horse racing club run by the community. The club has been incorporateds for 30 years. This Ball will be a celebration of that anniversary.

Target Market(s)

Middlemount Community

Industry/Entity Type

Club

Font styles to use
Serif
Decorative

Colors
1b1b1b
fbfbfb
6b449b
886aae
a64599
ffc214

Requirements
Must have
• Include
• where when time and cost
• ticket inclusions
• entertainement by Colin Hartwell
Nice to have
• Attached are some images for inspiration.
• It would be nice to have the race club logo included somewhere however not prominant.
Should not have
• Abstract geometriic lines
• images of people
• primary colours

```html
<!DOCTYPE html>
<html lang="en">
<head>
<meta charset="utf-8">
<title>Fernhollow Turf Society 30th Anniversary Ball</title>
<link rel="stylesheet" href="https://fonts.googleapis.com/css2?family=Great+Vibes&family=Kaushan+Script&family=Raleway:wght@600&display=swap">
<style>
  :root {
    --ink: #1b1b1b;
    --paper: #fbfbfb;
    --violet-deep: #6b449b;
    --lavender: #886aae;
    --magenta: #a64599;
    --gold: #ffc214;
  }
  html, body {
    margin: 0;
    padding: 0;
    overflow: hidden;
    background: var(--paper);
  }
  .poster {
    position: relative;
    width: 854px;
    height: 1200px;
    overflow: hidden;
    background: radial-gradient(ellipse 70% 55% at 50% 52%, var(--violet-deep) 0%, #7f459d 55%, var(--magenta) 100%);
    color: var(--paper);
  }
  .hero-art {
    position: absolute;
    left: 131px;
    top: 52px;
    width: 600px;
    height: 560px;
  }
  .headline {
    position: absolute;
    left: 0;
    width: 854px;
    margin: 0;
    text-align: center;
    font-weight: 400;
    line-height: 1;
    white-space: nowrap;
  }
  .club-name {
    top: 424px;
    font-family: "Great Vibes", cursive;
    font-size: 92px;
    letter-spacing: 2px;
  }
  .anniversary-number {
    top: 522px;
    font-family: "Kaushan Script", cursive;
    font-size: 52px;
  }
  .event-title {
    top: 590px;
    font-family: "Great Vibes", cursive;
    font-size: 108px;
  }
  .event-date {
    top: 712px;
    font-family: "Kaushan Script", cursive;
    font-size: 40px;
  }
  .event-venue {
    top: 794px;
    font-family: "Kaushan Script", cursive;
    font-size: 40px;
  }
  .ticket-details {
    position: absolute;
    left: 10px;
    top: 936px;
    margin: 0;
    font-family: "Raleway", sans-serif;
    font-weight: 600;
    font-size: 28px;
    line-height: 47px;
  }
  .club-mark {
    position: absolute;
    right: 14px;
    bottom: 22px;
    display: flex;
    align-items: center;
    gap: 8px;
    font-family: "Raleway", sans-serif;
    font-weight: 600;
    font-size: 12px;
    color: var(--paper);
  }
  .club-mark-dot {
    width: 40px;
    height: 40px;
    border-radius: 50%;
    background: var(--lavender);
  }
</style>
</head>
<body>
  <main class="poster">
    <svg class="hero-art" viewBox="0 0 600 560" role="img" aria-label="Illustration of a horseshoe with a leaping horse silhouette">
      <defs>
        <linearGradient id="heroFill" x1="0" y1="0" x2="1" y2="0.3">
          <stop offset="0%" stop-color="#886aae"/>
          <stop offset="55%" stop-color="#7d63a8"/>
          <stop offset="100%" stop-color="#1b1b1b"/>
        </linearGradient>
      </defs>
      <rect x="0" y="0" width="600" height="560" rx="280" fill="url(#heroFill)" opacity="0.85"/>
    </svg>

    <h1 class="headline club-name">Fernhollow Turf Society</h1>
    <p class="headline anniversary-number">30th</p>
    <p class="headline event-title">Anniversary Ball</p>
    <p class="headline event-date">28th April 2018 · 6:30pm till late</p>
    <p class="headline event-venue">at the Fernhollow Community Hall</p>

    <p class="ticket-details">
      Ticket Price : $120 , including<br>
      3 course dinner, drinks on arrival and<br>
      entertainment during the evening by Colin Hartwell.
    </p>

    <div class="club-mark">
      <span class="club-mark-dot"></span>
      <span>Fernhollow Turf Society</span>
    </div>
  </main>
</body>
</html>
```